Verdant QUICK Repairs Business card

Harbison Motors is looking for a business card design for our detailing wing "Verdant QUICK Repairs"
The services offered are vehicle paintless dent repairs, vehicle detailing, scratch and bumper repairs & paint and alloy wheel repairs.
Ideally the card design should be sharp, neat and professional. We are not looking for a card with pictures of cars.
Our corporate colours are blues (as in the logo supplied) which may look good with water droplets in high res and perhaps one or two images leaking off the card. Dark blacks with electric blues perhaps.
Images may be of a spray gun (we use Carrowmist), a rotary polisher (Trevalo Orbix) or similar objects used in the processes.

Industry/Entity Type

Paint

Contact Information for Business Card

Title: Verdant QUICK Repairs
Services: Bumper Repairs
Scratch/Paint Repairs
Paintless dent repairs
Alloy wheel repairs
Name: Martin K
Telephone: 0427195063
Email : martin@harbisonmotors.com.au

Font styles to use
Sans Serif
Other font styles liked:

Colors
0355a3
3277b5
0792cd
cfdfed

Requirements
Must have
• The title - "Verdant QUICK Repairs" should be a focus on either the from or back of the card
Should not have
• Photographs of cars

```html
<!DOCTYPE html>
<html lang="en">
<head>
<meta charset="utf-8">
<title>Verdant QUICK Repairs – Business Card</title>
<link rel="stylesheet" href="https://fonts.googleapis.com/css2?family=Open+Sans:wght@400;700;800&display=swap">
<style>
  :root {
    --page-bg: #e4e5e7;
    --card-white: #f4f5f6;
    --navy: #14285a;
    --deep-blue: #0a2a5e;
    --teal: #1ba3c9;
    --teal-light: #4fbfd8;
    --tab-grey: #b9bcc2;
    --back-black: #0c0c0d;
    --silver: #c8c9cb;
    --panel-text: #e8f3f8;
  }
  * { box-sizing: border-box; margin: 0; padding: 0; }
  html, body {
    width: 1200px; height: 1000px; overflow: hidden;
    background: var(--page-bg);
    font-family: "Open Sans", Arial, sans-serif;
  }
  .canvas {
    position: relative; width: 1200px; height: 1000px;
  }
  .card {
    position: absolute; left: 250px; width: 700px; height: 420px;
    overflow: hidden; box-shadow: 0 6px 18px rgba(0,0,0,.18);
  }

  /* Back of card */
  .card-back { top: 50px; background: var(--back-black); }
  .back-brand {
    position: absolute; inset: 0;
    display: flex; align-items: center; justify-content: center; gap: 22px;
  }
  .back-brand__dot {
    width: 56px; height: 56px; border-radius: 50%; background: var(--silver);
  }
  .back-brand__name {
    color: var(--silver); font-weight: 800; font-size: 50px;
    line-height: 1; text-transform: uppercase; letter-spacing: 1px;
  }

  /* Front of card */
  .card-front { top: 520px; background: var(--card-white); }
  .edge-tab {
    position: absolute; left: 0; top: 40px; width: 16px; height: 240px;
    background: linear-gradient(180deg, var(--teal) 0%, var(--deep-blue) 100%);
  }
  .edge-tab::after {
    content: ""; position: absolute; left: 16px; top: 132px;
    border-top: 14px solid transparent; border-bottom: 14px solid transparent;
    border-left: 14px solid var(--deep-blue);
  }
  .brand {
    position: absolute; left: 62px; top: 54px;
    display: flex; align-items: center; gap: 16px;
  }
  .brand__dot {
    width: 58px; height: 58px; border-radius: 50%; background: var(--navy);
  }
  .brand__name {
    color: var(--navy); font-weight: 800; font-size: 34px;
    line-height: 1; text-transform: uppercase; letter-spacing: .5px;
  }
  .contact {
    position: absolute; left: 62px; top: 190px; color: var(--navy);
  }
  .contact__name { font-weight: 800; font-size: 26px; margin-bottom: 22px; }
  .contact__line { font-size: 19px; line-height: 1.6; }

  .services {
    position: absolute; left: 400px; top: 0; right: 0; bottom: 0;
    background: linear-gradient(180deg, var(--teal) 0%, #0a6d9c 45%, var(--deep-blue) 100%);
  }
  .service-list {
    position: absolute; left: -48px; top: 78px; list-style: none;
  }
  .service {
    position: relative; display: flex; align-items: center;
    height: 48px; margin-bottom: 26px;
  }
  .service::before {
    content: ""; position: absolute; left: -6px; top: 34px;
    width: 60px; height: 10px; background: var(--tab-grey); opacity: .8;
  }
  .service__icon {
    position: relative; width: 48px; height: 48px; background: var(--teal-light);
    display: flex; align-items: center; justify-content: center;
  }
  .service__label {
    margin-left: 30px; color: var(--panel-text); font-size: 21px; white-space: nowrap;
  }
</style>
</head>
<body>
<div class="canvas">

  <section class="card card-back" aria-label="Card back">
    <div class="back-brand">
      <span class="back-brand__dot"></span>
      <span class="back-brand__name">Verdant Quick</span>
    </div>
  </section>

  <section class="card card-front" aria-label="Card front">
    <div class="edge-tab"></div>
    <div class="brand">
      <span class="brand__dot"></span>
      <span class="brand__name">Verdant<br>Quick</span>
    </div>
    <div class="contact">
      <p class="contact__name">Martin K</p>
      <p class="contact__line">T : 0427195063</p>
      <p class="contact__line">E : martin@harbisonmotors.com.au</p>
    </div>

    <div class="services">
      <ul class="service-list">
        <li class="service">
          <span class="service__icon">
            <svg width="30" height="30" viewBox="0 0 30 30" aria-hidden="true">
              <circle cx="15" cy="15" r="14" fill="#0d2b5c"/>
              <path d="M19.5 8.5a4.5 4.5 0 0 0-5.6 5.6l-5.2 5.2 1.9 1.9 5.2-5.2a4.5 4.5 0 0 0 5.6-5.6l-2.5 2.5-2-.4-.4-2z" fill="#4fbfd8"/>
            </svg>
          </span>
          <span class="service__label">Bumper Repairs</span>
        </li>
        <li class="service">
          <span class="service__icon">
            <svg width="30" height="30" viewBox="0 0 30 30" aria-hidden="true">
              <circle cx="15" cy="15" r="14" fill="#0d2b5c"/>
              <path d="M19.5 8.5a4.5 4.5 0 0 0-5.6 5.6l-5.2 5.2 1.9 1.9 5.2-5.2a4.5 4.5 0 0 0 5.6-5.6l-2.5 2.5-2-.4-.4-2z" fill="#4fbfd8"/>
            </svg>
          </span>
          <span class="service__label">Scratch/Paint Repairs</span>
        </li>
        <li class="service">
          <span class="service__icon">
            <svg width="30" height="30" viewBox="0 0 30 30" aria-hidden="true">
              <circle cx="15" cy="15" r="14" fill="#0d2b5c"/>
              <path d="M19.5 8.5a4.5 4.5 0 0 0-5.6 5.6l-5.2 5.2 1.9 1.9 5.2-5.2a4.5 4.5 0 0 0 5.6-5.6l-2.5 2.5-2-.4-.4-2z" fill="#4fbfd8"/>
            </svg>
          </span>
          <span class="service__label">Paintless dent repairs</span>
        </li>
        <li class="service">
          <span class="service__icon">
            <svg width="30" height="30" viewBox="0 0 30 30" aria-hidden="true">
              <circle cx="15" cy="15" r="14" fill="#0d2b5c"/>
              <path d="M19.5 8.5a4.5 4.5 0 0 0-5.6 5.6l-5.2 5.2 1.9 1.9 5.2-5.2a4.5 4.5 0 0 0 5.6-5.6l-2.5 2.5-2-.4-.4-2z" fill="#4fbfd8"/>
            </svg>
          </span>
          <span class="service__label">Alloy wheel repairs</span>
        </li>
      </ul>
    </div>
  </section>

</div>
</body>
</html>
```